Redesign of WordHarbor.com in Bootstrap 4

Current design of WordHarbor.com is not responsive. We need to change it to latest version of Bootstrap 4 keeping essential elements in place.

Apart from home page, we need designs for http://www.wordharbor.com/meaning/cat also.

Coding

Coded - Design and coding required

Number of Pages Required

2 page

Colors
34a7d8

Requirements
Must have
• Bootstrap 4

```html
<!DOCTYPE html>
<html lang="en">
<head>
<meta charset="utf-8">
<title>Word Harbor – Home</title>
<link href="https://fonts.googleapis.com/css2?family=Open+Sans:wght@400;600;700&display=swap" rel="stylesheet">
<style>
:root{
  --orange:#f7941d;
  --ink:#222222;
  --muted:#555555;
  --grey:#9a9a9a;
  --field:#ececec;
  --btn-blue:#3f6c9c;
  --footer:#6aa2d2;
  --hero-top:#f2f2f2;
  --hero-bot:#d9d9d9;
  --brand-blue:#1e5fae;
}
*{box-sizing:border-box;margin:0;padding:0}
html,body{width:1200px;height:3103px;overflow:hidden;background:#fff}
body{position:relative;font-family:"Open Sans",Arial,sans-serif;color:var(--ink)}
.abs{position:absolute}
.brand{left:0;width:1200px;top:62px;text-align:center}
.brand-mark{display:inline-flex;align-items:center;gap:16px;font-size:46px;font-weight:700;color:var(--brand-blue);line-height:1}
.brand-dot{width:30px;height:30px;border-radius:50%;background:var(--orange)}
.login-field{top:211px;height:38px;background:var(--field);color:#fff;font-size:17px;text-align:center;line-height:38px;letter-spacing:.5px}
.login-btn{left:799px;top:211px;width:66px;height:38px;background:var(--orange);color:#fff;font-size:16px;line-height:38px;text-align:center}
.nav a{position:absolute;top:286px;font-size:22px;color:#444;text-decoration:none;letter-spacing:.3px}
.nav a.active{color:var(--orange);border-top:3px solid var(--orange);padding-top:0;top:281px}
.nav a.register{left:991px;top:279px;width:132px;height:46px;line-height:46px;text-align:center;background:#e8e8e8}
.hero{left:0;top:352px;width:1200px;height:511px;background:linear-gradient(180deg,var(--hero-top),var(--hero-bot) 60%,#e6e6e6)}
.hero-lines{left:0;width:1200px;top:430px;text-align:center;font-size:28px;line-height:39.5px;color:#2a2a2a}
.search-input{left:205px;top:716px;width:687px;height:47px;background:#fff;color:#aaa;font-size:20px;line-height:47px;padding-left:30px}
.search-btn{left:892px;top:716px;width:132px;height:47px;background:var(--orange);color:#fff;font-size:21px;font-weight:700;line-height:47px;text-align:center}
.feature-img{left:288px;width:327px}
.feature-title{font-size:27px;font-weight:700;color:var(--orange)}
.feature-text{width:340px;font-size:22px;line-height:30px;color:#222}
.feature-text.small{font-size:20px;line-height:29px;width:320px}
.feature-btn{width:116px;height:37px;background:var(--btn-blue);color:#fff;font-size:16px;font-weight:700;line-height:37px;text-align:center}
.browse-title{left:0;width:1200px;top:2500px;text-align:center;font-size:25px;font-weight:600;color:var(--grey)}
.alphabet{left:97px;width:1006px;top:2556px;display:flex;justify-content:space-between;font-size:25px;font-weight:600;color:var(--grey)}
.footer{left:0;top:2675px;width:1200px;height:428px;background:var(--footer);color:#fff}
.footer-tagline{left:180px;top:2752px;font-size:23px;line-height:30px}
.footer-col{top:2846px;font-size:23px;line-height:30px}
.footer-col h4{font-size:25px;font-weight:700;margin-bottom:28px}
</style>
</head>
<body>

<div class="abs brand"><span class="brand-mark"><span class="brand-dot"></span>Word Harbor</span></div>

<div class="abs login-field" style="left:364px;width:182px">USERNAME</div>
<div class="abs login-field" style="left:579px;width:178px">PASSWORD</div>
<div class="abs login-btn">LOGIN</div>

<nav class="nav">
  <a class="active" style="left:70px">HOME</a>
  <a style="left:182px">IDIOMS</a>
  <a style="left:308px">COMMON ERRORS</a>
  <a style="left:552px">CROSSWORD</a>
  <a style="left:743px">BLOG</a>
  <a style="left:852px">CONTACT</a>
  <a class="register">REGISTER</a>
</nav>

<section class="abs hero" role="img" aria-label="Soft blurred background of open books"></section>
<div class="abs hero-lines">
  Search from more than 300,000 words and phrases<br>
  Multiple usages to clarify the context<br>
  Audio, phonetics, meanings, synonyms and antonyms<br>
  Save the words to your personal deck and access from anywhere<br>
  It's FREE
</div>
<div class="abs search-input">ENTER A WORD OR PHASE</div>
<div class="abs search-btn">SEARCH</div>

<div class="abs feature-img" style="top:933px;height:323px;background:linear-gradient(160deg,#e8cdb3,#c9a27e)" role="img" aria-label="Open book on a table"></div>
<div class="abs feature-title" style="left:660px;top:926px">English Tidbit</div>
<div class="abs feature-text small" style="left:660px;top:988px">o "gibe" is to taunt. Gibe is however slowly going out of use. Jibe means to agree but is often used in the negative sense. Although the versions of the tricksters jibed, the police officer suspected that there was something wrong.</div>

<div class="abs feature-img" style="top:1312px;height:320px;background:linear-gradient(135deg,#d6d6d6,#8a8a8a)" role="img" aria-label="Crossword puzzle with a pen"></div>
<div class="abs feature-title" style="left:662px;top:1304px">Crossword Lovers!</div>
<div class="abs feature-text" style="left:662px;top:1365px;width:320px">Take this daily crossword challenge from Word Harbor.</div>
<div class="abs feature-btn" style="left:877px;top:1595px">SOLVE NOW</div>

<div class="abs feature-img" style="top:1730px;height:320px;background:radial-gradient(circle at 45% 50%,#3a6fb0,#e87a2a 55%,#f0f0f0 80%)" role="img" aria-label="Browser add-on puzzle illustration"></div>
<div class="abs feature-title" style="left:660px;top:1722px">Blazewing Addon</div>
<div class="abs feature-text" style="left:660px;top:1783px;width:330px">Add this tool to your Blazewing and quickly look up for definitions from any website without leaving the page.</div>
<div class="abs feature-btn" style="left:877px;top:2015px">GET IT NOW</div>

<div class="abs feature-img" style="left:306px;top:2121px;width:265px;height:262px;background:linear-gradient(135deg,#e9e9ef,#5b6c9a 55%,#1c1c1c)" role="img" aria-label="Three smartphones showing the app"></div>
<div class="abs feature-title" style="left:656px;top:2106px">Designed for PocketOne</div>
<div class="abs feature-text" style="left:656px;top:2167px;width:320px">Word Harbor is specially designed for your PocketOne to quickly lookup meaining, usages and audio of words.</div>

<div class="abs browse-title">Browse Dictionary</div>
<div class="abs alphabet">
  <span>A</span><span>B</span><span>C</span><span>D</span><span>E</span><span>F</span><span>G</span><span>H</span><span>I</span><span>J</span><span>K</span><span>L</span><span>M</span><span>N</span><span>O</span><span>P</span><span>Q</span><span>R</span><span>S</span><span>T</span><span>U</span><span>V</span><span>W</span><span>X</span><span>Z</span><span>Y</span>
</div>

<footer class="abs footer"></footer>
<div class="abs footer-tagline" style="color:#fff">Word Harbor Dictionary: Meaning/Definition, Audio,<br>Phonetics, Usages and more</div>
<div class="abs footer-col" style="left:180px;color:#fff"><h4>WordHarbor.com</h4>FAQ<br>Contact<br>Blog</div>
<div class="abs footer-col" style="left:521px;color:#fff"><h4>Legal</h4>Privacy Policy<br>Terms of Use</div>
<div class="abs footer-col" style="left:817px;color:#fff;width:230px"><h4>Others</h4>Popular Words<br>Common Errors in English<br>Exam Prep Online</div>

</body>
</html>
```